Modern looking signage for dental office.

Exterior signage for passing cars
Updates
Need extra days to review
Target Market(s)
Cars passing by
Font styles to use
Sans Serif
Colors
3276b5
Requirements
Must have
- Logo
- OPEN ON SUTURDAY AND SUNDAY
- NIGHT CLINIC AVAILABLE
- PLEASE USE THE FONT TYPE IN FILE 4 UPLOADED BELOW.
- (847) 302-4496
- Modern looking

```html
<!DOCTYPE html>
<html lang="en">
<head>
<meta charset="utf-8">
<title>Alder Dental – Exterior Sign</title>
<link rel="stylesheet" href="https://fonts.googleapis.com/css2?family=Montserrat:wght@400&family=Questrial&family=Roboto+Condensed:wght@300&family=Varela+Round&family=Nunito+Sans:wght@800&display=swap">
<style>
  :root {
    --page-bg: #ffffff;
    --panel-bg: #f2f2f2;
    --brand-grey: #555253;
    --accent-teal: #17809a;
    --edge-blue: #106f98;
    --deep-blue: #116d98;
    --glow-teal: #1a9a94;
    --white: #ffffff;
  }
  html, body {
    margin: 0;
    width: 1200px;
    height: 1000px;
    overflow: hidden;
    background: var(--page-bg);
  }
  .sign { display: block; width: 1200px; height: 1000px; }
  .brand-name { font-family: "Montserrat", sans-serif; font-weight: 400; fill: var(--brand-grey); }
  .brand-tagline { font-family: "Roboto Condensed", sans-serif; font-weight: 300; fill: var(--brand-grey); }
  .night-title { font-family: "Nunito Sans", sans-serif; font-weight: 800; fill: var(--accent-teal); }
  .night-sub { font-family: "Questrial", sans-serif; fill: var(--accent-teal); }
  .phone-number { font-family: "Varela Round", sans-serif; fill: var(--accent-teal); }
  .open-label { font-family: "Nunito Sans", sans-serif; font-weight: 800; fill: var(--white); }
  .open-days { font-family: "Questrial", sans-serif; fill: var(--white); }
</style>
</head>
<body>
<svg class="sign" viewBox="0 0 1200 1000" xmlns="http://www.w3.org/2000/svg">
  <defs>
    <radialGradient id="days-glow" cx="955" cy="510" r="260" gradientUnits="userSpaceOnUse">
      <stop offset="0" stop-color="var(--glow-teal)"/>
      <stop offset="1" stop-color="var(--deep-blue)"/>
    </radialGradient>
    <filter id="days-shadow" x="-10%" y="-20%" width="120%" height="140%">
      <feDropShadow dx="2" dy="3" stdDeviation="0.6" flood-color="#0b3f52" flood-opacity="0.6"/>
    </filter>
  </defs>

  <!-- sign board -->
  <rect class="board" x="63" y="177" width="1062" height="653" fill="var(--panel-bg)"/>
  <rect class="board-edge" x="63" y="177" width="17" height="653" fill="var(--edge-blue)"/>

  <!-- weekend panel -->
  <path class="days-panel" d="M845 177 C741 380 741 630 845 830 L1125 830 L1125 177 Z" fill="url(#days-glow)"/>

  <!-- brand -->
  <circle class="brand-mark" cx="180" cy="312" r="72" fill="none" stroke="var(--brand-grey)" stroke-width="2.5"/>
  <text class="brand-name" x="265" y="343" font-size="88" textLength="505" lengthAdjust="spacingAndGlyphs">ALDER DENTAL</text>
  <text class="brand-tagline" x="314" y="388" font-size="30" textLength="390" lengthAdjust="spacingAndGlyphs">MODERN GENERAL DENTISTRY</text>

  <!-- night clinic -->
  <text class="night-title" x="274" y="530" font-size="42" textLength="311" lengthAdjust="spacingAndGlyphs">NIGHT CLINIC</text>
  <text class="night-sub" x="326" y="586" font-size="44" textLength="218" lengthAdjust="spacingAndGlyphs">AVAILABLE</text>

  <!-- phone -->
  <g class="phone-icon">
    <circle cx="210" cy="748" r="28" fill="none" stroke="var(--accent-teal)" stroke-width="4"/>
    <path d="M205 730 h7 l2 9 l-5 3 q0 8 5 15 l5 -2 l3 8 l-6 4 q-16 -8 -16 -29 z" fill="var(--accent-teal)"/>
  </g>
  <text class="phone-number" x="262" y="765" font-size="58" textLength="410" lengthAdjust="spacingAndGlyphs">(847) 302-4496</text>

  <!-- weekend hours -->
  <g class="days-copy" filter="url(#days-shadow)">
    <text class="open-label" x="864" y="431" font-size="38" textLength="178" lengthAdjust="spacingAndGlyphs">Open on</text>
    <text class="open-days" x="815" y="537" font-size="56" textLength="262" lengthAdjust="spacingAndGlyphs">Saturday</text>
    <text class="open-days" x="890" y="590" font-size="56" textLength="113" lengthAdjust="spacingAndGlyphs">and</text>
    <text class="open-days" x="845" y="643" font-size="56" textLength="216" lengthAdjust="spacingAndGlyphs">Sunday</text>
  </g>
</svg>
</body>
</html>
```